Business Card Design

Verdessa is a floral design company for weddings and special events.
Colours wanted are dark grey, aqua blue, white and black.
dark grey for the background, and the Verdessa in the aqua blue, rest of the writing in white and black etc.

Our floral design style is Rustic, textural, natural,
Wanting some kind of simplistic flower symbol next to the Verdessa see pictures.

Hi im so sorry I've changed some criteria. been confused on how this site works and what i want!! hope this is more straight forward. I also need clip art of the simple floral design i attached for my web site and also car magnets. thank you thank you thank YOU!!!! cherrs Bree

I have attached x5 ideas on where to place the lotus flower next to and around the verdessa. please use simliar colours of the flower as pictured. please cut out the white back ground from the flower. use only petals. use only lotus or the other icon provided per idea. still deciding on which one to use so waiting to see what looks best with your designs. thank you so very much in advance.!! Kindest REgards Bree

hi i am currently getting a logo design made through this also so can we wait until it is complete before any revisions are made. sorry about the delay!! thank you thank you thank you!! kind regards Bree

Reason: im having a logo made also to use on the cards. please hold off on any designs until this is received. thank you and so sorry about this!! cheers bR

Target Market(s)

modern elegant professional

Industry/Entity Type

Floral

Contact Information for Business Card

Front:
verdessa floral design (all lower case) floral design in smaller writting)
www.verdessafloraldesign.example.au

Back:
Wedding and event design

Bridget - 0498265140
verdessa@mailcove.example.au
Pauline-0455839061
floristpaulinecrowe@postly.example.com

Noosa-Tewantin, Sunshine coast, Qld

Font styles to use
Other font styles liked:
• corben, cookie

Colors
87d0c7
34b8a4
eaf2ce
ffffff
e4daeb
cfdeed

Requirements
Must have
• ; dark grey for back ground. or possible all white?
;verdessa floral designs in lower case and in blue' green aqua colour. all other writing in white.
icon which i can also use on the website. see pictures(i want to use the same on my web site.. if you can please make me an clip art icon also?
Nice to have
• simple elegant, earthy, flower icon
or second option icon of lotus looking flower verdessa inside
fonts please: verdessa floral design in (corben)
all writing on the back in (cookie)
maybe have the same icon clip art provided faintly on the back, bold on the front?
i also need car magnets to

```html
<!DOCTYPE html>
<html lang="en">
<head>
<meta charset="utf-8">
<title>Verdessa Floral Designs – Business Cards</title>
<link rel="stylesheet" href="https://fonts.googleapis.com/css2?family=Corben:wght@400;700&family=Montserrat:wght@400;500;600&display=swap">
<style>
  :root {
    --backdrop: #e2e2e2;
    --card-black: #1f1f21;
    --aqua: #34b8c9;
    --aqua-deep: #2aa3b3;
    --band-grey: #b9b9bb;
    --ink-white: #ffffff;
    --ink-dark: #1a1a1a;
  }
  * { box-sizing: border-box; margin: 0; padding: 0; }
  html, body { width: 1200px; height: 907px; overflow: hidden; }
  body {
    background: var(--backdrop);
    font-family: "Montserrat", sans-serif;
    position: relative;
  }

  .card {
    position: absolute;
    width: 520px;
    height: 300px;
    background: var(--card-black);
    box-shadow: 0 10px 24px rgba(0,0,0,0.22);
    overflow: hidden;
  }

  /* Back of card */
  .card--back { left: 180px; top: 90px; }
  .card--back .frame {
    position: absolute;
    inset: 22px;
    border: 3px solid var(--aqua);
  }
  .card--back .brand {
    position: absolute;
    inset: 0;
    display: flex;
    align-items: center;
    justify-content: center;
    gap: 14px;
  }
  .brand-dot {
    width: 34px;
    height: 34px;
    border: 3px solid var(--aqua);
    border-radius: 50%;
  }
  .brand-name {
    font-family: "Corben", serif;
    color: var(--aqua);
    font-weight: 400;
    line-height: 1;
  }
  .card--back .brand-name { font-size: 44px; }

  /* Front of card */
  .card--front { left: 500px; top: 470px; }
  .front-brand {
    position: absolute;
    left: 30px;
    top: 34px;
    width: 190px;
    text-align: center;
  }
  .front-brand .brand-dot {
    margin: 0 auto 10px;
    width: 48px;
    height: 48px;
  }
  .front-brand .brand-name { font-size: 34px; letter-spacing: 1px; }
  .front-brand .brand-sub {
    font-family: "Corben", serif;
    color: var(--aqua);
    font-size: 13px;
    letter-spacing: 1px;
    margin-top: 4px;
  }

  .name-band {
    position: absolute;
    left: 240px;
    right: 0;
    top: 40px;
    height: 52px;
    background: var(--aqua);
    padding: 8px 16px;
    color: var(--ink-dark);
  }
  .name-band .person {
    font-size: 17px;
    font-weight: 600;
    letter-spacing: 0.5px;
    text-transform: uppercase;
    line-height: 1.1;
  }
  .name-band .role { font-size: 13px; font-weight: 500; }

  .contact {
    position: absolute;
    left: 256px;
    top: 104px;
    color: var(--ink-white);
    font-size: 10.5px;
    line-height: 1.45;
    letter-spacing: 0.3px;
  }
  .contact .group { margin-bottom: 7px; }

  .base-band {
    position: absolute;
    left: 0;
    bottom: 0;
    width: 520px;
    height: 110px;
  }
</style>
</head>
<body>

  <section class="card card--back" aria-label="Business card back">
    <div class="frame"></div>
    <div class="brand">
      <span class="brand-dot"></span>
      <span class="brand-name">verdessa</span>
    </div>
  </section>

  <section class="card card--front" aria-label="Business card front">
    <div class="front-brand">
      <div class="brand-dot"></div>
      <div class="brand-name">verdessa</div>
      <div class="brand-sub">floral designs</div>
    </div>

    <div class="name-band">
      <div class="person">Bridget Ashvale</div>
      <div class="role">Managing Director</div>
    </div>

    <div class="contact">
      <div class="group">
        <div>0498 265 140</div>
        <div>0455 839 061</div>
      </div>
      <div class="group">
        <div>verdessa@mailcove.example.au</div>
        <div>www.verdessafloraldesign.example.au</div>
      </div>
      <div class="group">
        <div>Shop 4 Lakeside Walk</div>
        <div>Riverside Road QLD</div>
      </div>
    </div>

    <svg class="base-band" viewBox="0 0 520 110" aria-hidden="true">
      <polygon points="0,40 520,72 520,110 0,110" fill="var(--band-grey)"/>
      <polygon points="0,34 520,66 520,74 0,42" fill="var(--aqua)"/>
      <!-- phone -->
      <g transform="translate(300,52)">
        <circle r="12" fill="var(--aqua)"/>
        <path d="M-4,-5 l2,-1 l2,3 l-1.5,1.5 q1,3 3.5,4.5 l1.5,-1.5 l3,2 l-1,2 q-6,1 -9.5,-6.5 z" fill="#fff"/>
      </g>
      <!-- globe -->
      <g transform="translate(380,57)">
        <circle r="12" fill="var(--aqua)"/>
        <circle r="6" fill="none" stroke="#fff" stroke-width="1.4"/>
        <ellipse rx="2.6" ry="6" fill="none" stroke="#fff" stroke-width="1.2"/>
        <line x1="-6" y1="0" x2="6" y2="0" stroke="#fff" stroke-width="1.2"/>
      </g>
      <!-- pin -->
      <g transform="translate(460,62)">
        <circle r="12" fill="var(--aqua)"/>
        <path d="M0,7 C-4,2 -5,-1 -5,-2.5 A5,5 0 0 1 5,-2.5 C5,-1 4,2 0,7 z" fill="#fff"/>
        <circle cy="-2.5" r="1.8" fill="var(--aqua)"/>
      </g>
    </svg>
  </section>

</body>
</html>
```